Business Card for Marco Tindley Analytics and Marco Tindley Photography

I want a double sided business card: on one side it should be about "Marco Tindley Photography" and on the other side about "Marco Tindley Analytics". You find the logos for these two projects in the attachments. The design of the business card should blend well with the colours and fonts used in the logos and should be quite simple, yet look professional and modern.

In addition to my name, there should be content for a telephone number, e-mail address and website. There should be little icons (for telephone, email and web) before these fields. I do not want a postal mail address field.
Lastly you should indicate that people can contact me in the following languages: Lëtzebuergesch, Deutsch, Français, English, Castellano, Ido
This should be very unobtrusive: either in a small muted font or with little icons (preferably without using flags as flags represent nations, not languages - one possibility would be by using the 2 letter ISO codes).

The design should be delivered in Adobe Illustrator format or something similar that I can edit easily, as it's possible that I will change my e-mail address and domain soon.

I hope this was detailed enough but still leaves you some freedom for designing something nice.

Thank you!
Marco

Industry/Entity Type

Business

Contact Information for Business Card

e-mail address: mjt_@fernpost.example
website: www.marcotindley.example (for Marco Tindley Photography)
website: quarrynet.example/mjt (for Marco Tindley Analytics - this address is likely to change)
phone: +352 648 907 215 (not my real number - I prefer not to publish it on the web)

Requirements
Nice to have
• A speech bubble followed by the 2-letter language codes (lb, de, fr, en, es, io) or even speech bubble icons for every language would be nice and eliminates the need to put text like 'you can contact me in the following languages'.

```html
<!DOCTYPE html>
<html lang="en">
<head>
<meta charset="utf-8">
<title>Marco Tindley — Business Cards</title>
<link rel="stylesheet" href="https://fonts.googleapis.com/css2?family=Crimson+Pro:wght@400;600&display=swap">
<style>
  :root {
    --stage: #0d0d0d;
    --paper: #f8f6f1;
    --ink-dark: #2a2a2a;
    --green: #1f9a4a;
    --green-light: #8cc63f;
    --orange: #ef7d22;
    --yellow: #fbc318;
    --night: #0a0a0a;
    --web-green: #1b9a4a;
  }
  html, body {
    margin: 0;
    width: 1200px;
    height: 1000px;
    overflow: hidden;
    background: var(--stage);
    font-family: "Crimson Pro", Georgia, serif;
  }
  .stage {
    position: relative;
    width: 1200px;
    height: 1000px;
  }
  .card {
    position: absolute;
    width: 540px;
    height: 310px;
    border-radius: 18px;
    overflow: hidden;
    box-shadow: 0 18px 40px rgba(0,0,0,.6);
  }
  .card-analytics { left: 40px; top: 300px; background: var(--paper); }
  .card-photo { left: 620px; top: 390px; background: var(--night); }

  .edge-band {
    position: absolute;
    left: 0; right: 0; bottom: 0;
    height: 16px;
  }
  .card-analytics .edge-band { background: linear-gradient(90deg, var(--green), var(--green-light)); }
  .card-photo .edge-band { background: linear-gradient(90deg, var(--orange), var(--yellow)); }

  /* Analytics side */
  .brand-analytics {
    position: absolute;
    left: 36px; top: 70px;
    display: flex; align-items: center; gap: 12px;
  }
  .brand-mark {
    width: 22px; height: 22px;
    background: var(--green);
  }
  .brand-name {
    font-size: 26px;
    font-weight: 400;
    color: var(--orange);
    line-height: 1.1;
    width: 200px;
  }
  .contact {
    position: absolute;
    left: 300px; top: 120px;
  }
  .contact-name {
    font-size: 27px;
    font-weight: 600;
    color: var(--green);
    margin: 0 0 8px;
  }
  .contact-list { list-style: none; margin: 0; padding: 0; }
  .contact-list li {
    display: flex; align-items: center; gap: 8px;
    font-size: 17px;
    font-weight: 600;
    color: var(--ink-dark);
    line-height: 1.35;
  }
  .icon { width: 13px; height: 13px; flex: none; }
  .languages {
    position: absolute;
    left: 36px; top: 238px;
    display: flex; align-items: center; gap: 8px;
    font-size: 18px;
    font-weight: 600;
    color: var(--ink-dark);
  }
  .bubble { width: 24px; height: 22px; }

  /* Photography side */
  .photo-content {
    position: absolute;
    left: 0; right: 0; top: 0; bottom: 16px;
    display: flex;
    flex-direction: column;
    align-items: center;
    justify-content: center;
    gap: 34px;
    padding-top: 20px;
    box-sizing: border-box;
  }
  .brand-photo {
    font-size: 38px;
    font-weight: 400;
    color: var(--orange);
    line-height: 1.05;
    white-space: nowrap;
  }
  .web-photo {
    display: flex; align-items: center; gap: 10px;
    font-size: 24px;
    color: var(--web-green);
  }
  .web-photo .icon { width: 20px; height: 20px; }
</style>
</head>
<body>
<main class="stage">

  <section class="card card-analytics" aria-label="Analytics side">
    <div class="brand-analytics">
      <span class="brand-mark"></span>
      <span class="brand-name">Marco Tindley Analytics</span>
    </div>

    <div class="contact">
      <p class="contact-name">Marco Tindley</p>
      <ul class="contact-list">
        <li>
          <svg class="icon" viewBox="0 0 16 16" aria-hidden="true"><path fill="#ef7d22" d="M3 1l3 3-1.5 2a9 9 0 0 0 5.5 5.5L12 10l3 3-2 2C7 15 1 9 1 3z"/></svg>
          1 (212) 555-0147
        </li>
        <li>
          <svg class="icon" viewBox="0 0 16 16" aria-hidden="true"><rect x="1" y="3" width="14" height="10" fill="#ef7d22"/><path d="M1 3l7 6 7-6" fill="none" stroke="#f8f6f1" stroke-width="1.4"/></svg>
          mjt_@fernpost.example
        </li>
        <li>
          <svg class="icon" viewBox="0 0 16 16" aria-hidden="true"><circle cx="8" cy="8" r="7" fill="#ef7d22"/><path d="M1 8h14M8 1c-3 3-3 11 0 14M8 1c3 3 3 11 0 14" fill="none" stroke="#f8f6f1" stroke-width="1"/></svg>
          www.marcotindley.example
        </li>
      </ul>
    </div>

    <div class="languages">
      <svg class="bubble" viewBox="0 0 24 22" aria-hidden="true"><path fill="#1f9a4a" d="M12 1C6 1 1 4.8 1 9.5c0 3 2 5.6 5 7.1L5 21l5-3.3c.7.1 1.3.1 2 .1 6 0 11-3.8 11-8.3S18 1 12 1z"/></svg>
      lb, de, fr, en, es, io
    </div>

    <div class="edge-band"></div>
  </section>

  <section class="card card-photo" aria-label="Photography side">
    <div class="photo-content">
      <div class="brand-photo">Marco Tindley Photography</div>
      <div class="web-photo">
        <svg class="icon" viewBox="0 0 16 16" aria-hidden="true"><circle cx="8" cy="8" r="7" fill="none" stroke="#ef7d22" stroke-width="1.4"/><path d="M1 8h14M8 1c-3 3-3 11 0 14M8 1c3 3 3 11 0 14" fill="none" stroke="#ef7d22" stroke-width="1"/></svg>
        www.MarcoTindley.example
      </div>
    </div>
    <div class="edge-band"></div>
  </section>

</main>
</body>
</html>
```